Kids Soccer club - Wordpress website

Wordpress site for kids soccer club. mobile friendly.
1.Link to google calandar nicely displayed- this week(upcoming events ) view on home page? separate page for detail. events to be updated by coaches by mobile.
2.Feed from club facebook page which parents might use more.
3. News page for coaches/ parents to post photos and info re matches etc.
4. Location Map and contact details

Target Market(s)

parents, kids, coaches involved in the club

Industry/Entity Type

Club

Coding

Coded - Design and coding required

Number of Pages Required

4 page

Requirements
Must have
• Pages:
• 1. Home
• 2. Club Calander
• 3. News
• 4. Location
• also a feed from the team facebook page
• and a space for sponsor details
• domain will be www.marrowfenrovers.com
• see that for further ideas on the brief

```html
<!DOCTYPE html>
<html lang="en">
<head>
<meta charset="utf-8">
<title>Club Calendar – Marrowfen Rovers F.C.</title>
<link rel="stylesheet" href="https://fonts.googleapis.com/css2?family=Roboto+Condensed:wght@400;700&family=Open+Sans:wght@400;600&family=Roboto:wght@400;500&display=swap">
<style>
:root{
  --green:#3a9a26;
  --green-dark:#2a7d1c;
  --green-footer:#2f8f22;
  --nav-active:#262b2c;
  --ink:#333;
  --muted:#777;
  --cal-blue:#2c4fa3;
  --cal-line:#c9d3e6;
  --cal-head:#e3e9f8;
  --today:#fff4cf;
  --today-bar:#f5c75a;
  --table-head:#e4e4e4;
  --table-alt:#f5f5f5;
}
*{box-sizing:border-box;margin:0;padding:0}
html,body{width:855px;height:1200px;overflow:hidden}
body{position:relative;font-family:"Open Sans",sans-serif;color:var(--ink);
  background:linear-gradient(180deg,#3b5360 0%,#5b7480 14%,#2e4a2c 30%,#1f5a17 45%,#12300d 75%,#0b1e08 100%)}
.abs{position:absolute}

/* header */
.social{top:40px;left:70px;display:flex;gap:3px}
.social span{width:22px;height:22px;border:1.5px solid #fff;border-radius:50%;display:block}
.btn{top:40px;height:20px;font:500 9px/18px "Roboto Condensed",sans-serif;color:#fff;text-align:center;border-radius:2px;letter-spacing:.3px}
.btn-join{left:662px;width:65px;background:var(--green);border:1px solid #5bbf44}
.btn-sign{left:726px;width:58px;border:1px solid #fff}

.nav{top:104px;left:70px;width:715px;height:37px;background:linear-gradient(180deg,#48aa30,var(--green-dark));border-bottom:2px solid #1f6a14}
.nav a{position:absolute;top:0;height:37px;font:400 11px/37px "Roboto Condensed",sans-serif;color:#fff;text-decoration:none;letter-spacing:.2px}
.nav .active{background:var(--nav-active);text-align:center}
.crest{top:20px;left:372px;width:112px;height:112px;border-radius:50%;background:#fff;border:3px solid var(--green);
  display:flex;align-items:center;justify-content:center;text-align:center;font:700 12px/1.2 "Roboto Condensed",sans-serif;color:var(--green-dark)}

.hero{top:142px;left:70px;width:715px;height:160px;
  background:linear-gradient(180deg,#6d7f8c 0%,#8a9a7f 35%,#4f7a3a 62%,#2d5f25 100%)}
.hero h1{position:absolute;top:62px;left:0;width:715px;text-align:center;font:700 29px/1 "Roboto Condensed",sans-serif;color:#fff;text-shadow:0 2px 4px rgba(0,0,0,.5);letter-spacing:.5px}

.page{top:302px;left:70px;width:715px;height:670px;background:#fff}
.page-shade{top:302px;left:140px;width:575px;height:24px;background:radial-gradient(ellipse at 50% 0,rgba(0,0,0,.16),rgba(0,0,0,0) 70%)}

/* calendar */
.cal{top:344px;left:120px;width:609px;height:368px;background:var(--cal-head);font-family:Arial,sans-serif}
.cal-bar{position:absolute;top:3px;left:2px;right:4px;height:13px;font-size:8px;display:flex;align-items:center}
.cal-bar .today{border:1px solid #aaa;background:#eee;padding:0 2px;font-size:7px}
.cal-bar .arr{width:17px;height:10px;background:#5b7fd6;margin-left:2px}
.cal-bar .month{font-weight:bold;margin-left:5px;font-size:8.5px}
.cal-bar .tabs{margin-left:auto;display:flex;gap:8px;color:var(--cal-blue)}
.cal-bar .tabs b{color:#222;background:#fff;padding:0 3px}
.cal-days{position:absolute;top:17px;left:6px;width:597px;display:grid;grid-template-columns:repeat(7,1fr);font-size:7px;color:var(--cal-blue);text-align:center}
.cal-grid{position:absolute;top:26px;left:6px;width:597px;height:323px;background:#fff;display:grid;grid-template-columns:repeat(7,1fr);grid-template-rows:repeat(5,1fr);border-top:1px solid var(--cal-line)}
.day{border-right:1px solid var(--cal-line);border-bottom:1px solid var(--cal-line);position:relative;font-size:7px}
.day .n{display:block;text-align:right;padding:1px 2px;background:#eef2fb;color:#555}
.day .n.off{color:#aaa}
.day.now{background:var(--today)}
.day.now .n{background:var(--today-bar)}
.ev{display:block;padding:3px 2px;color:var(--cal-blue);font-size:7px;letter-spacing:.2px;white-space:nowrap}
.ev b{font-size:6px}
.cal-foot{position:absolute;top:354px;left:6px;font-size:6.5px;color:#333}
.cal-brand{position:absolute;top:350px;right:6px;background:#fff;border:1px solid #ccc;font-size:7.5px;padding:1px 3px;color:#666}
.cal-brand i{display:inline-block;width:8px;height:8px;background:#4a77d8;vertical-align:-1px;margin-right:2px}

/* this week */
.week-title{top:738px;left:120px;font:400 19px/1 "Roboto Condensed",sans-serif;color:#444}
.week{top:769px;left:122px;width:606px;height:172px;border-collapse:collapse;table-layout:fixed;font-family:"Roboto",sans-serif;border:1px solid #e2e2e2}
.week th{background:var(--table-head);height:37px;font:400 12px "Roboto",sans-serif;color:#333;text-align:left;padding-left:20px;border-right:1px solid #d8d8d8}
.week td{font-size:8.5px;line-height:12px;color:var(--muted);padding:0 0 0 20px;height:45px;border-right:1px solid #e2e2e2;vertical-align:middle;white-space:nowrap}
.week tbody tr:nth-child(even) td{background:var(--table-alt)}
.week td.side{background:#fff !important;border-right:none;padding:0}
.signup{top:849px;left:641px;width:77px;height:48px;background:linear-gradient(180deg,#4fae35,var(--green-dark));border-radius:3px;color:#fff;font:400 13px/14px "Roboto Condensed",sans-serif;display:flex;align-items:center;justify-content:center;text-align:center}

/* footer */
.footer{top:972px;left:70px;width:715px;height:187px;background:var(--green-footer);color:#fff}
.f-crest{position:absolute;top:30px;left:22px;width:100px;height:100px;border-radius:50%;background:#fff;color:var(--green-dark);display:flex;align-items:center;justify-content:center;text-align:center;font:700 11px/1.2 "Roboto Condensed",sans-serif}
.f-h{position:absolute;top:26px;font:400 14.5px/1 "Roboto Condensed",sans-serif;text-transform:uppercase}
.f-text{position:absolute;top:54px;left:169px;width:180px;font-size:8.3px;line-height:14px;white-space:nowrap}
.f-mail{position:absolute;top:104px;left:170px;font-size:8.5px;line-height:16px}
.f-mail svg{position:absolute;left:0;top:2px}
.f-mail div{padding-left:26px}
.f-map{position:absolute;top:53px;left:364px;width:198px;height:105px;border:3px solid #fff;background:linear-gradient(135deg,#dcdcdc,#c9c9c9 60%,#d6d6d6)}
.f-links{position:absolute;top:58px;left:608px;list-style:none;font-size:8.5px;line-height:15.2px}
.f-links li::before{content:"";display:inline-block;border-left:4px solid #fff;border-top:3px solid transparent;border-bottom:3px solid transparent;margin-right:8px}
.copy{top:1174px;left:0;width:855px;text-align:center;color:#fff;font-size:8.5px}
</style>
</head>
<body>

<div class="abs social" aria-label="Social links"><span></span><span></span></div>
<div class="abs btn btn-join">JOIN NOW</div>
<div class="abs btn btn-sign">SIGN IN</div>

<nav class="abs nav">
  <a style="left:24px">HOME</a>
  <a style="left:92px">ABOUT US</a>
  <a class="active" style="left:163px;width:111px">CLUB CALANADER</a>
  <a style="left:457px">NEWS</a>
  <a style="left:518px">LOCATION</a>
  <a style="left:599px">CONTACT US</a>
</nav>
<div class="abs crest">Marrowfen<br>Rovers F.C.</div>

<div class="abs hero" role="img" aria-label="Photo of a coach watching young players train on an artificial pitch">
  <h1>CLUB CALENDAR</h1>
</div>

<div class="abs page"></div>
<div class="abs page-shade"></div>

<section class="abs cal">
  <div class="cal-bar">
    <span class="today">Today</span><span class="arr"></span><span class="arr"></span>
    <span class="month">September 2016 ▾</span>
    <span class="tabs"><span style="color:#222">Print</span><span>Week</span><b>Month</b><span>Agenda</span></span>
  </div>
  <div class="cal-days"><span>Sun</span><span>Mon</span><span>Tue</span><span>Wed</span><span>Thu</span><span>Fri</span><span>Sat</span></div>
  <div class="cal-grid">
    <div class="day"><span class="n off">28</span></div>
    <div class="day"><span class="n off">29</span></div>
    <div class="day"><span class="n off">30</span></div>
    <div class="day"><span class="n off">31</span><span class="ev"><b>7pm</b> U14 Training</span></div>
    <div class="day"><span class="n">Sep 1</span><span class="ev"><b>6pm</b> U13 Training</span></div>
    <div class="day"><span class="n">2</span></div>
    <div class="day"><span class="n">3</span></div>

    <div class="day"><span class="n">4</span></div>
    <div class="day"><span class="n">5</span><span class="ev"><b>7pm</b> U12 Training</span></div>
    <div class="day"><span class="n">6</span></div>
    <div class="day"><span class="n">7</span><span class="ev"><b>7pm</b> U14 Training</span></div>
    <div class="day now"><span class="n">8</span><span class="ev"><b>6pm</b> U13 Training</span></div>
    <div class="day"><span class="n">9</span><span class="ev"><b>7pm</b> Registration Night</span></div>
    <div class="day"><span class="n">10</span></div>

    <div class="day"><span class="n">11</span></div>
    <div class="day"><span class="n">12</span></div>
    <div class="day"><span class="n">13</span></div>
    <div class="day"><span class="n">14</span><span class="ev"><b>7pm</b> U14 Training</span></div>
    <div class="day"><span class="n">15</span><span class="ev"><b>6pm</b> U13 Training</span></div>
    <div class="day"><span class="n">16</span></div>
    <div class="day"><span class="n">17</span></div>

    <div class="day"><span class="n">18</span></div>
    <div class="day"><span class="n">19</span></div>
    <div class="day"><span class="n">20</span></div>
    <div class="day"><span class="n">21</span><span class="ev"><b>7pm</b> U14 Training</span></div>
    <div class="day"><span class="n">22</span><span class="ev"><b>6pm</b> U13 Training</span></div>
    <div class="day"><span class="n">23</span></div>
    <div class="day"><span class="n">24</span></div>

    <div class="day"><span class="n">25</span></div>
    <div class="day"><span class="n">26</span></div>
    <div class="day"><span class="n">27</span></div>
    <div class="day"><span class="n">28</span><span class="ev"><b>7pm</b> U14 Training</span></div>
    <div class="day"><span class="n">29</span><span class="ev"><b>6pm</b> U13 Training</span></div>
    <div class="day"><span class="n">30</span></div>
    <div class="day"><span class="n off">Oct 1</span></div>
  </div>
  <div class="cal-foot">Events shown in time zone: Dublin</div>
  <div class="cal-brand"><i></i>Club Calendar</div>
</section>

<h2 class="abs week-title">THIS WEEK</h2>
<table class="abs week">
  <colgroup><col style="width:89px"><col style="width:79px"><col style="width:86px"><col style="width:81px"><col style="width:87px"><col style="width:86px"><col style="width:98px"></colgroup>
  <thead><tr><th>Monday</th><th>Tuesday</th><th>Wednesday</th><th>Thursday</th><th>Friday</th><th>Saturday</th><th style="border-right:none"></th></tr></thead>
  <tbody>
    <tr><td>U14 Training<br>7:00pm</td><td>U14 Training<br>7:00pm</td><td>U14 Training<br>7:00pm</td><td>U14 Training<br>7:00pm</td><td>U14 Training<br>7:00pm</td><td>U14 Training<br>7:00pm</td><td class="side" rowspan="3"></td></tr>
    <tr><td>U14 Training<br>7:00pm</td><td>U14 Training<br>7:00pm</td><td>U14 Training<br>7:00pm</td><td>U14 Training<br>7:00pm</td><td>U14 Training<br>7:00pm</td><td>U14 Training<br>7:00pm</td></tr>
    <tr><td>U14 Training<br>7:00pm</td><td>U14 Training<br>7:00pm</td><td>U14 Training<br>7:00pm</td><td>U14 Training<br>7:00pm</td><td>U14 Training<br>7:00pm</td><td>U14 Training<br>7:00pm</td></tr>
  </tbody>
</table>
<div class="abs signup">Signup<br>to Calander</div>

<footer class="abs footer">
  <div class="f-crest">Marrowfen<br>Rovers F.C.</div>
  <h3 class="f-h" style="left:168px">Contact Us</h3>
  <p class="f-text">Marrowfen Rovers FC<br>Heatherlow Park, Marrowfen, Kilbrannock<br>Ardmoy Co. Westmere.</p>
  <div class="f-mail">
    <svg width="14" height="10" viewBox="0 0 14 10"><rect x=".5" y=".5" width="13" height="9" fill="none" stroke="#fff"/><path d="M.5.5 7 6 13.5.5" fill="none" stroke="#fff"/></svg>
    <div>Email:<br>hello@marrowfenrovers.com</div>
  </div>
  <h3 class="f-h" style="left:363px">Our Location</h3>
  <div class="f-map" role="img" aria-label="Map showing the club grounds"></div>
  <h3 class="f-h" style="left:607px;top:28px">Quick Links</h3>
  <ul class="f-links">
    <li>Home</li><li>About Us</li><li>Club Calendar</li><li>News</li><li>Location</li><li>Contact Us</li>
  </ul>
</footer>

<p class="abs copy">2016 © Marrowfen Rovers FC.All Rights Reserved</p>

</body>
</html>
```